wood grain ultrasonic essential oil aroma diffuser

Design a package that is simple but luxurious for the diffuser with my logo. My business is called “Kindle the Moss”. The logo incorporates “Thoughts become things” the concept is positive thinking. I don’t particularly want the product featured as I have like to develop a uniform look for packaging and website and there are 2 different diffusers,

Target Market(s)

People interested in yoga, meditation, metaphysical aspects

Industry/Entity Type

Health And Wellness

Colors

Designer to choose colors to be used in the design.

Requirements
Must have
• Luxurious feel to packaging and alignment with the website

```html
<!DOCTYPE html>
<html lang="en">
<head>
<meta charset="utf-8">
<title>Kindle the Moss — Ultrasonic Oil Diffuser Packaging</title>
<link rel="stylesheet" href="https://fonts.googleapis.com/css2?family=Montserrat:wght@300;400;500&display=swap">
<style>
  :root{
    --teal:#1fb0c4;
    --teal-deep:#1596a8;
    --white:#ffffff;
    --ink:#2a2a2a;
    --page:#e9eaeb;
    --wood-dark:#3a2a24;
    --wood-light:#e58a2c;
  }
  *{box-sizing:border-box;margin:0;padding:0}
  html,body{width:1200px;height:780px;overflow:hidden;background:var(--page);font-family:"Montserrat",sans-serif}
  .canvas{position:relative;width:1200px;height:780px}
  .panel{position:absolute;overflow:hidden}

  /* top flap */
  .panel-top{left:150px;top:60px;width:300px;height:140px;background:var(--white)}
  .panel-top .brand{position:absolute;left:18px;top:18px;display:flex;align-items:center;gap:8px;color:var(--ink);font-size:15px;font-weight:300}
  .top-visual{position:absolute;right:0;top:40px;width:170px;height:60px;border-radius:60px 0 0 6px;background:linear-gradient(90deg,#6b5047,var(--wood-dark))}

  .brand-dot{width:14px;height:14px;border-radius:50%;background:currentColor;flex:none}

  /* front panel */
  .panel-front{left:150px;top:200px;width:300px;height:480px}
  .front-photo{position:absolute;inset:0;background:linear-gradient(160deg,#f3f1ee 0%,#d9d3cc 45%,#b7aca2 70%,#ece9e6 100%)}
  .front-product{position:absolute;left:212px;top:300px;width:58px;height:84px;border-radius:40% 40% 30% 30%/60% 60% 30% 30%;background:linear-gradient(90deg,#4a372f,var(--wood-dark))}
  .brand-tag{position:absolute;right:24px;top:20px;width:72px;height:72px;background:var(--teal);color:var(--white);display:flex;flex-direction:column;align-items:center;justify-content:center;gap:6px;font-size:8.5px;font-weight:300;text-align:center;line-height:1.1}
  .title{color:var(--white);font-weight:300;line-height:1}
  .front-title{position:absolute;right:20px;top:112px;text-align:right}
  .front-title .line-1{font-size:40px;letter-spacing:.5px}
  .front-title .line-2{font-size:25px;margin-top:4px}
  .feature-band{position:absolute;left:0;top:210px;width:100%;height:86px;background:var(--teal);padding:12px 0 0 118px;color:var(--white);font-size:17px;font-weight:300;line-height:1.3}
  .front-icons{position:absolute;left:18px;bottom:20px;display:flex;gap:16px}

  .icon{display:flex;flex-direction:column;align-items:center;gap:3px;color:var(--white);font-size:7px;text-align:center;line-height:1.1}
  .icon svg{width:30px;height:30px}

  /* teal side panel */
  .panel-side{left:450px;top:200px;width:300px;height:480px;background:var(--teal)}
  .side-brand{position:absolute;left:92px;top:26px;display:flex;flex-direction:column;align-items:center;gap:8px;color:var(--white);font-size:13px;font-weight:300}
  .side-brand .brand-dot{width:40px;height:40px;border:2px solid var(--white);background:transparent}
  .side-icons{position:absolute;left:16px;top:100px;display:flex;flex-direction:column;gap:12px;width:40px}
  .badge-hours{width:36px;height:36px;border:2px solid var(--white);border-radius:50%;display:flex;align-items:center;justify-content:center;color:var(--white);font-size:16px;font-weight:400}
  .badge-hours small{font-size:6px}
  .side-product{position:absolute;left:48px;top:150px;width:160px;height:300px;border-radius:46% 46% 22% 22%/62% 62% 20% 20%;background:linear-gradient(90deg,#f2a552,var(--wood-light) 55%,#c86f1e)}
  .side-wordmark{position:absolute;right:-4px;top:20px;height:460px;writing-mode:vertical-rl;transform:rotate(180deg);color:var(--white);font-size:60px;font-weight:300;line-height:1;text-align:left;white-space:nowrap}

  /* info panel */
  .panel-info{left:750px;top:200px;width:300px;height:480px;background:#f5f1ee}
  .info-photo-top{position:absolute;inset:0 0 auto 0;height:230px;background:linear-gradient(110deg,#ede6e1 0%,#c9a08a 55%,#8a5a44 100%)}
  .info-photo-bottom{position:absolute;inset:auto 0 0 0;height:110px;background:linear-gradient(180deg,#f3f0ee,#cfc8c3)}
  .info-brand{position:absolute;left:130px;top:30px;display:flex;flex-direction:column;align-items:center;gap:6px;color:var(--white);font-size:10px;font-weight:300}
  .info-brand .brand-dot{width:26px;height:26px}
  .info-title{position:absolute;left:80px;top:96px;text-align:center}
  .info-title .line-1{font-size:32px}
  .info-title .line-2{font-size:20px;margin-top:2px}
  .info-copy{position:absolute;left:0;top:188px;width:100%;height:190px;background:rgba(255,255,255,.88);display:grid;grid-template-columns:1fr 1fr;gap:14px;padding:18px 14px;color:var(--ink);font-size:8.6px;line-height:1.45;text-align:justify}
</style>
</head>
<body>
<main class="canvas">

  <section class="panel panel-top" aria-label="Top flap">
    <div class="brand"><span class="brand-dot"></span>Kindle the Moss</div>
    <div class="top-visual" role="img" aria-label="Tip of the dark wood grain diffuser"></div>
  </section>

  <section class="panel panel-front" aria-label="Front panel">
    <div class="front-photo" role="img" aria-label="Bright modern living room interior with the diffuser on a shelf"></div>
    <div class="front-product" role="img" aria-label="Dark wood grain diffuser releasing mist"></div>
    <div class="brand-tag"><span class="brand-dot"></span>Kindle the Moss</div>
    <h1 class="title front-title"><div class="line-1">Ultrasonic</div><div class="line-2">Oil Diffuser</div></h1>
    <div class="feature-band">Relaxing<br>Quiet Sound<br>Smooth Design</div>
    <div class="front-icons">
      <div class="icon">
        <svg viewBox="0 0 30 30" fill="none" stroke="currentColor" stroke-width="1.6"><rect x="6" y="4" width="18" height="22" rx="3"/><line x1="6" y1="11" x2="24" y2="11"/></svg>350ml
      </div>
      <div class="icon">
        <svg viewBox="0 0 30 30" fill="none" stroke="currentColor" stroke-width="1.6"><rect x="4" y="4" width="22" height="22" rx="3"/><path d="M11 21c-3-4 3-6 0-11M16 21c-3-4 3-6 0-11M21 21c-3-4 3-6 0-11"/></svg>Covering area<br>269-323sq.ft
      </div>
      <div class="icon">
        <svg viewBox="0 0 30 30" fill="none" stroke="currentColor" stroke-width="1.6"><rect x="3" y="3" width="24" height="24" rx="4"/><path d="M9 14a6 6 0 0 1 11-3M21 16a6 6 0 0 1-11 3"/><path d="M20 7v4h-4M10 23v-4h4"/></svg>Cycle
      </div>
    </div>
  </section>

  <section class="panel panel-side" aria-label="Side panel">
    <div class="side-brand"><span class="brand-dot"></span>Kindle the Moss</div>
    <div class="side-icons">
      <div class="icon">
        <svg viewBox="0 0 30 30" fill="none" stroke="currentColor" stroke-width="1.6"><rect x="6" y="4" width="18" height="22" rx="3"/><line x1="6" y1="11" x2="24" y2="11"/></svg>350ml
      </div>
      <div class="icon">
        <svg viewBox="0 0 30 30" fill="none" stroke="currentColor" stroke-width="1.6"><rect x="4" y="4" width="22" height="22" rx="3"/><path d="M11 21c-3-4 3-6 0-11M16 21c-3-4 3-6 0-11M21 21c-3-4 3-6 0-11"/></svg>Covering area<br>269-323sq.ft
      </div>
      <div class="icon">
        <svg viewBox="0 0 30 30" fill="none" stroke="currentColor" stroke-width="1.6"><rect x="3" y="3" width="24" height="24" rx="4"/><path d="M9 14a6 6 0 0 1 11-3M21 16a6 6 0 0 1-11 3"/><path d="M20 7v4h-4M10 23v-4h4"/></svg>Cycle
      </div>
      <div class="badge-hours"><small>up to</small>12<small>hr</small></div>
    </div>
    <div class="side-product" role="img" aria-label="Light wood grain tulip shaped diffuser"></div>
    <div class="side-wordmark">Kindle the Moss</div>
  </section>

  <section class="panel panel-info" aria-label="Information panel">
    <div class="info-photo-top" role="img" aria-label="Woman relaxing with eyes closed in warm light"></div>
    <div class="info-photo-bottom" role="img" aria-label="Soft focus white coffee cup"></div>
    <div class="info-brand"><span class="brand-dot"></span>Kindle the Moss</div>
    <h2 class="title info-title"><div class="line-1">Ultrasonic</div><div class="line-2">Oil Diffuser</div></h2>
    <div class="info-copy">
      <p>Lorem ipsum dolor sit amet, consecLorem ipsum dolor sit amet, consectetuer adipiscing elit, sed diam nonummy nibh euismod tincidunt ut laoreet dolore magna Lorem ipsum dolor sit amet, consectetuer adipiscing elit, Lorem ipsum dolor sit amet, consectetuer adipiscing elit, sed diam nonummy nibh euismod tincidunt ut laoreet</p>
      <p>Lorem ipsum dolor sit amet, consecLorem ipsum dolor sit amet, consectetuer adipiscing elit, sed diam nonummy nibh euismod tincidunt ut laoreet dolore magna Lorem ipsum dolor sit amet, consectetuer adipiscing elit, Lorem ipsum dolor sit amet, consectetuer adipiscing elit, sed diam nonummy nibh euismod tincidunt ut laoreet</p>
    </div>
  </section>

</main>
</body>
</html>
```